New Packaging Design Project

Dear Talented designers,
We are going to manufacturing in Spain, depilatory cold wax strips for hair removal, under our private label:
We will have Two Types:
1- Type one for Normal and dray skin , main ingredients are with Aloevera and Argan Oil.
2- Type Two for sensitive skin, main ingredients are Rose hip oil and mixed berries and essential oils.
3- Each pack containing 24 wax strips+4 after depilatory wipes+ instruction leaflet
4- Brand name will be "SilkaVeen".
5- I prefer the green color to be the main color for the Normal dry skin type also feel free to use any other matched colors in addition to green as a main color, and Mauve and pink for the sensitive type , also feel free to use any other matched colors in addition to Mauve and pink as a main color.
6- Kindly we need to add some golden effects, lines, to the design to show some luxury.
7- Also Kindly I need to design a countertop display stand, it will contains 12 packs , 6 packs of each type.
8- Kindly you will find attached file only to have an Idea about the product, it is only a guide , and you do not have to follow it , Kindly I need an innovative attractive designs.
9- Kindly we need to use illustration symbols as shown on Fern crest brand attached , like dermatologicaly tested symbol , contains Natural active ingredients symbol, etc…
10- Also attached is the claims must be on the packs with English and please consider leaving a space for Arabic Language ( we will put it locally after you make it with English) as it will be with both Arabic and English .
11- Also Attached the packs layouts.
Warmest regards.
Dr.K. Tolun
Executive manager.
Nawal Sidra trading Est.
Riyadh- Saudi Arabia
Email: tolun.karim@mailvera.com
Cell: +966531274085
Skype: k.tolun8
Updates
Dear Talented designers,
In addition to breif sent with my project, kindly consider that Silkaveen ( Our brand name) kindly need it to looks big as it is our brand, moreover, kindly need the Silkaveen to be with Two different matched colors, exactly like PixelGuild logo , but of course with Two different matched colors , not Black and Blue .
Warmest regards.
Dr. K. Tolun
Saudi Arabia
Saudi Arabia
The product for women
Hair

```html
<!DOCTYPE html>
<html lang="en">
<head>
<meta charset="utf-8">
<title>SilkaVeen Cold Wax Strips – Pack Front</title>
<link href="https://fonts.googleapis.com/css2?family=Questrial&family=Open+Sans:wght@600;700&display=swap" rel="stylesheet">
<style>
  :root {
    --stage: #e4e6e8;
    --mint-top: #eef6e4;
    --leaf-mid: #b6dc84;
    --leaf-low: #7cbd3e;
    --forest: #1d6a36;
    --forest-deep: #145a2b;
    --lime-type: #6cb32e;
    --gold: #d9b24a;
    --gold-light: #f3d77c;
    --white: #ffffff;
  }
  * { margin: 0; padding: 0; box-sizing: border-box; }
  html, body { width: 1200px; height: 960px; overflow: hidden; }
  body {
    background: var(--stage);
    font-family: "Questrial", "Century Gothic", sans-serif;
    position: relative;
  }
  .pack-front {
    position: absolute;
    left: 370px; top: 40px;
    width: 460px; height: 880px;
    background: linear-gradient(180deg, var(--mint-top) 0%, #dcedc4 35%, var(--leaf-mid) 62%, var(--leaf-low) 100%);
    overflow: hidden;
  }
  .brand-name {
    position: absolute; top: 70px; left: 0; width: 100%;
    text-align: center;
    font-size: 68px; line-height: 1.1;
    color: var(--forest);
    letter-spacing: 1px;
  }
  .title-line-one {
    position: absolute; top: 178px; left: 0; width: 100%;
    text-align: center;
    font-size: 58px; color: var(--lime-type); line-height: 1;
  }
  .title-line-two {
    position: absolute; top: 238px; left: 0; width: 100%;
    text-align: center;
    font-size: 100px; color: var(--forest); line-height: 1;
    letter-spacing: 1px;
  }
  .ingredient-line {
    position: absolute; top: 368px; left: 0; width: 100%;
    text-align: center;
    font-family: "Open Sans", Arial, sans-serif; font-weight: 700;
    font-size: 17px; color: var(--forest);
  }
  .ingredient-art {
    position: absolute; top: 440px; left: 70px;
    width: 360px; height: 250px;
    border-radius: 50%;
    background: radial-gradient(ellipse at 55% 50%, #9a5a2c 0%, #b57a44 25%, #5fa63a 55%, rgba(124,189,62,0) 75%);
  }
  .skin-type-tab {
    position: absolute; left: 0; top: 420px;
    width: 46px; height: 300px;
    background: var(--forest);
    border-radius: 0 8px 8px 0;
  }
  .skin-type-tab span {
    position: absolute; left: 50%; top: 50%;
    transform: translate(-50%, -50%) rotate(-90deg);
    white-space: nowrap;
    font-family: "Open Sans", Arial, sans-serif; font-weight: 600;
    font-size: 16px; color: var(--white);
  }
  .claim-badges {
    position: absolute; top: 728px; left: 60px;
    width: 380px; display: flex; justify-content: space-between;
  }
  .claim-badge { width: 84px; height: 84px; }
  .pack-footer {
    position: absolute; left: 0; bottom: 0;
    width: 100%; height: 56px;
    background: var(--forest);
    display: flex; align-items: center; justify-content: center; gap: 8px;
    color: var(--white);
    font-family: "Open Sans", Arial, sans-serif;
  }
  .strip-count { font-weight: 700; font-size: 20px; }
  .strip-extra-lead { font-weight: 700; font-size: 13px; }
  .strip-extra { font-weight: 600; font-size: 15px; }
</style>
</head>
<body>
<main class="pack-front">
  <div class="brand-name">SilkaVeen</div>
  <div class="title-line-one">COLD WAX</div>
  <div class="title-line-two">STRIPS</div>
  <div class="ingredient-line">with Aloevera and Argan Oil</div>

  <div class="ingredient-art" role="img" aria-label="Illustration of split argan nuts resting on aloe vera leaves"></div>

  <div class="skin-type-tab"><span>For Normal and Dry skin</span></div>

  <div class="claim-badges">
    <svg class="claim-badge" viewBox="0 0 84 84" aria-label="Dermatologically tested">
      <defs><path id="arc-derm" d="M8,42 A34,34 0 0,1 76,42"/></defs>
      <circle cx="42" cy="42" r="40" fill="var(--forest-deep)"/>
      <circle cx="42" cy="44" r="24" fill="none" stroke="var(--gold)" stroke-width="2.5"/>
      <text font-family="Open Sans, sans-serif" font-size="5.6" font-weight="700" fill="var(--gold-light)"><textPath href="#arc-derm" startOffset="50%" text-anchor="middle">DERMATOLOGICALLY TESTED</textPath></text>
      <path d="M31 45 L39 53 L55 34" fill="none" stroke="var(--gold)" stroke-width="5" stroke-linecap="round" stroke-linejoin="round"/>
    </svg>
    <svg class="claim-badge" viewBox="0 0 84 84" aria-label="Contains natural active ingredients">
      <defs><path id="arc-nat" d="M8,42 A34,34 0 0,1 76,42"/></defs>
      <circle cx="42" cy="42" r="40" fill="var(--forest-deep)"/>
      <circle cx="42" cy="44" r="24" fill="none" stroke="var(--gold)" stroke-width="2.5"/>
      <text font-family="Open Sans, sans-serif" font-size="5" font-weight="700" fill="var(--gold-light)"><textPath href="#arc-nat" startOffset="50%" text-anchor="middle">CONTAINS NATURAL ACTIVE INGREDIENTS</textPath></text>
      <path d="M31 56 C31 39 42 31 55 31 C55 46 46 56 31 56 Z M31 56 L46 41" fill="var(--gold)" stroke="var(--forest-deep)" stroke-width="1.5"/>
    </svg>
    <svg class="claim-badge" viewBox="0 0 84 84" aria-label="Effective on short hairs">
      <defs><path id="arc-hair" d="M8,42 A34,34 0 0,1 76,42"/></defs>
      <circle cx="42" cy="42" r="40" fill="var(--forest-deep)"/>
      <circle cx="42" cy="44" r="24" fill="none" stroke="var(--gold)" stroke-width="2.5"/>
      <text font-family="Open Sans, sans-serif" font-size="5.8" font-weight="700" fill="var(--gold-light)"><textPath href="#arc-hair" startOffset="50%" text-anchor="middle">EFFECTIVE ON SHORT HAIRS</textPath></text>
      <circle cx="42" cy="46" r="13" fill="var(--gold)" role="img" aria-label="Hair follicle diagram"/>
    </svg>
    <svg class="claim-badge" viewBox="0 0 84 84" aria-label="Zero percent allergens, parabens and SLS">
      <defs><path id="arc-zero" d="M8,42 A34,34 0 0,1 76,42"/></defs>
      <circle cx="42" cy="42" r="40" fill="var(--forest-deep)"/>
      <circle cx="42" cy="44" r="24" fill="none" stroke="var(--gold)" stroke-width="2.5"/>
      <text font-family="Open Sans, sans-serif" font-size="5.8" font-weight="700" fill="var(--gold-light)"><textPath href="#arc-zero" startOffset="50%" text-anchor="middle">ALLERGENS - PARABENS - SLS</textPath></text>
      <text x="42" y="53" text-anchor="middle" font-family="Questrial, sans-serif" font-size="24" fill="var(--gold)">0%</text>
    </svg>
  </div>

  <footer class="pack-footer">
    <span class="strip-count">24 STRIPS</span>
    <span class="strip-extra-lead">PLUS</span>
    <span class="strip-extra">x4 after depilatory wipes</span>
  </footer>
</main>
</body>
</html>
```